Law Firm Advertising Design Needed

Law Office of Dorvel K Tansy provides legal services to businesses and individuals who have been or are being injured. Our main practice area is personal injury (car accidents, wrongful death, premises liability), but we are looking for an ad that highlights a lesser known area of our practice - insurance company bad faith and breach of contract.

This ad will be placed in 8 1/2" x 11" format in a local neighborhood directory. It will also be placed in a smaller format (to be determined) in the local newspaper of a region of Arizona that has recently lost a considerable number of homes and people to wildfire.

We want to convey through the ad that our firm is available to help if their insurance company is not paying a legitimate claim or not paying enough for their claim.

Because of the tragic nature of the events in Yarnell, we would like to avoid images of fire or anything resembling fire. However, the ad should capture the attention of individuals who are struggling through an insurance claim with all the stacks of paperwork and frustrated with unresponsive adjusters and unreasonably low offers.

The design should convey a feeling of safety, security and being taken care of.

Information that must be included in the ad are: the firm name (Law Office of Dorvel K Tansy), address (4857 W 17th Avenue, Ste 406, Phoenix, AZ 85033), the phone number (602-574-2930) and the fact that we have mobile offices available to assist in your area.

An example of text that has been used in the past is here:
"If your own insurance company is refusing to pay what you are owed on a claim, call the Law Office of Dorvel K Tansy. We fight for you by examining the reasons your insurance carrier is denying or making an insufficient offer on the claim; updating and correcting claim documentation; making a new demand and filing a lawsuit if necessary. Whether it's a simple misunderstanding or something more complicated, we can help!

Here are a few of the kinds of claims we handle:
- Hit and Run or Uninsured driver claims
- Fire, flood and property loss
- Life insurance benefits
- Health insurance claims
- Catastrophic losses
- Business insurance
- Wrongful Death Benefits

Our attorneys are available to help you cut through the nonsense. Call to make an appointment for a free consultation with an attorney today. "

An example of a previous ad for car accident services is attached for reference.
Updates

Hi Everyone,

The main lawyer involved in the decision making process has been giving me some feedback in general on the designs that I thought I would pass along.  He does not want the name of the law firm to be the first thing you notice when you look at the ad. Try to keep that small and possibly to the bottom of the ad. The phone number should be rather large, but the address should be rather small (we are required by the State Bar to include our address, but we don't want our location to limit the location of our clients because our mobile offices can travel to them).  He would prefer that the logo either not be included or be not a significant part of the ad.

                                   

Thanks!  I will continue providing individual feedback to ads received. 

Target Market(s)

Low to middle income residents of the State of Arizona with little or no college education

Industry/Entity Type

Insurance

```html
<!DOCTYPE html>
<html lang="en">
<head>
<meta charset="utf-8">
<title>Is Your Insurance Company Refusing To Pay? – Law Office of Dorvel K Tansy</title>
<link rel="stylesheet" href="https://fonts.googleapis.com/css2?family=Arimo:wght@400&family=Tinos:wght@400;700&display=swap">
<style>
  :root {
    --navy: #17306d;
    --navy-deep: #0f2356;
    --navy-band: #1b3374;
    --bronze: #8d5718;
    --body-ink: #1b1b1b;
    --gold-caps: #e6c88f;
    --desk: #efe6d6;
    --bg-light: #f6f6f2;
    --bg-mid: #dfe3da;
    --photo-tone-a: #c9cfc4;
    --photo-tone-b: #a8b3b6;
    --box-edge: #b9b9b9;
  }
  * { margin: 0; padding: 0; box-sizing: border-box; }
  html, body { width: 932px; height: 1200px; overflow: hidden; }
  body { background: #ffffff; }

  .ad {
    position: relative;
    width: 932px;
    height: 1200px;
    overflow: hidden;
    background: radial-gradient(ellipse at 20% 30%, var(--bg-light) 0%, #eef0ea 45%, var(--bg-mid) 100%);
    font-family: "Arimo", Arial, sans-serif;
  }

  .hero-photo {
    position: absolute;
    left: 500px;
    top: 200px;
    width: 432px;
    height: 760px;
    background:
      radial-gradient(ellipse at 60% 35%, rgba(214,196,160,0.55) 0%, rgba(214,196,160,0) 45%),
      radial-gradient(ellipse at 55% 75%, rgba(168,179,182,0.7) 0%, rgba(168,179,182,0) 60%),
      linear-gradient(180deg, rgba(201,207,196,0) 0%, var(--photo-tone-a) 40%, var(--photo-tone-b) 100%);
    border-radius: 220px 0 0 0;
    opacity: 0.85;
  }

  .backdrop {
    position: absolute;
    left: 0; top: 0;
    width: 932px; height: 1200px;
  }

  .headline {
    position: absolute;
    left: 49px;
    top: 74px;
    font-family: "Tinos", "Times New Roman", serif;
  }
  .headline-kicker {
    display: block;
    font-size: 41px;
    line-height: 48px;
    color: var(--bronze);
  }
  .headline-main {
    display: block;
    font-size: 67px;
    line-height: 74px;
    color: var(--navy);
  }
  .headline-main strong { font-weight: 700; }

  .intro {
    position: absolute;
    left: 49px;
    top: 226px;
    width: 402px;
    font-size: 16.5px;
    line-height: 26px;
    color: var(--body-ink);
    text-align: justify;
  }

  .invite {
    position: absolute;
    left: 49px;
    top: 493px;
    font-family: "Tinos", "Times New Roman", serif;
    font-size: 20px;
    line-height: 24.8px;
    color: var(--bronze);
  }

  .phone {
    position: absolute;
    left: 47px;
    top: 628px;
    font-family: "Tinos", "Times New Roman", serif;
    font-size: 51px;
    line-height: 60px;
    color: var(--navy);
  }

  .claim-box {
    position: absolute;
    left: 49px;
    top: 757px;
    width: 290px;
    height: 264px;
    background: #ffffff;
    border: 2px solid var(--box-edge);
    border-radius: 12px;
    box-shadow: 0 2px 6px rgba(0,0,0,0.18);
    padding: 26px 0 0 16px;
    list-style: none;
    font-family: "Tinos", "Times New Roman", serif;
    font-size: 17.5px;
    line-height: 27px;
    color: var(--navy);
  }
  .claim-box li { padding-left: 12px; text-indent: -12px; }
  .claim-box li.wrap { line-height: 23px; margin-bottom: 4px; }

  .firm {
    position: absolute;
    left: 0;
    top: 1050px;
    width: 932px;
    text-align: center;
    font-family: "Tinos", "Times New Roman", serif;
    color: #ffffff;
  }
  .firm-name {
    font-size: 43px;
    line-height: 50px;
  }
  .firm-name em { font-style: italic; }
  .firm-address {
    font-size: 18.5px;
    line-height: 24px;
  }
  .firm-mobile {
    font-size: 19px;
    line-height: 30px;
    letter-spacing: 0.5px;
    color: var(--gold-caps);
  }
</style>
</head>
<body>
<main class="ad">
  <div class="hero-photo" role="img" aria-label="Photograph of a stressed woman at a desk holding her head while reading an insurance letter, with stacks of paperwork in front of her"></div>

  <svg class="backdrop" width="932" height="1200" viewBox="0 0 932 1200" aria-hidden="true">
    <defs>
      <linearGradient id="deskTone" x1="0" y1="0" x2="1" y2="0">
        <stop offset="0" stop-color="#f7f2e8"/>
        <stop offset="1" stop-color="#e9dfcc"/>
      </linearGradient>
      <linearGradient id="bandTone" x1="0" y1="0" x2="0" y2="1">
        <stop offset="0" stop-color="#2a4187"/>
        <stop offset="0.35" stop-color="#1b3374"/>
        <stop offset="1" stop-color="#0f2356"/>
      </linearGradient>
    </defs>
    <path d="M0 820 C 240 790, 560 860, 932 930 L 932 1000 L 0 1000 Z" fill="url(#deskTone)"/>
    <path d="M0 940 C 300 960, 620 1000, 932 1030 L 932 1200 L 0 1200 Z" fill="url(#bandTone)"/>
  </svg>

  <h1 class="headline">
    <span class="headline-kicker">Is Your Insurance Company</span>
    <span class="headline-main"><strong>REFUSING</strong> To Pay?</span>
  </h1>

  <p class="intro">If your own insurance company is refusing to pay what you are owed on a claim, call the Law Office of Dorvel K Tansy. We fight for you by examining the reasons your insurance carrier is denying or making an insufficient offer on the claim; updating and correcting claim documentation; making a new demand and filing a lawsuit if necessary. Whether it's a simple misunderstanding or something more complicated, we can help!</p>

  <p class="invite">Our attorneys are available to<br>help you cut through the nonsense.<br>Call to make an appointment<br>for a FREE consultation with<br>an attorney today.</p>

  <p class="phone">602-574-2930</p>

  <ul class="claim-box">
    <li class="wrap">- Hit and Run or<br>Uninsured driver claims</li>
    <li>- Fire, flood and property loss</li>
    <li>- Life insurance benefits</li>
    <li>- Health insurance claims</li>
    <li>- Catastrophic losses</li>
    <li>- Business insurance</li>
    <li>- Wrongful Death Benefits</li>
  </ul>

  <footer class="firm">
    <p class="firm-name">Law Office <em>of</em> Dorvel K Tansy</p>
    <p class="firm-address">4857 W 17th Avenue, Ste 406, Phoenix, AZ 85033</p>
    <p class="firm-mobile">MOBILE OFFICES AVAILABLE TO ASSIST IN YOUR AREA</p>
  </footer>
</main>
</body>
</html>
```